Lumenfield Holdings

Professional looking business card using darker colours
I do not yet have a logo for the company so feel free to suggest
The business is based on consultancy and project management
Based in Melbourne
Business card can omit the word "Holdings" and can be Lumenfield Consulting etc.

Business

Contact Name on card : Tom Verisco Contact number : +61412 305 617 Email address will be confirmed shortly.

```html
<!DOCTYPE html>
<html lang="en">
<head>
<meta charset="utf-8">
<title>Lumenfield Consulting — Business Card</title>
<link rel="stylesheet" href="https://fonts.googleapis.com/css2?family=Jost:wght@300;500&family=Source+Sans+3:wght@400;600&display=swap">
<style>
  :root {
    --stage-top: #2a2a2a;
    --stage-bottom: #050505;
    --card-white: #ffffff;
    --brand-blue: #2a66bb;
    --blue-light: #417bc6;
    --blue-deep: #1a5dae;
    --ink: #333333;
    --mark-grey: #8a8a8a;
    --tag-grey: #6f6f6f;
  }
  * { box-sizing: border-box; margin: 0; padding: 0; }
  html, body { width: 1200px; height: 900px; overflow: hidden; }
  body {
    background: linear-gradient(to bottom, var(--stage-top), var(--stage-bottom));
    font-family: "Source Sans 3", sans-serif;
    position: relative;
  }
  .card {
    position: absolute;
    top: 306px;
    width: 440px;
    height: 271px;
    border-radius: 10px;
  }
  .card-front { left: 149px; background: var(--card-white); }
  .card-back {
    left: 608px;
    background: linear-gradient(to bottom, var(--blue-light), var(--blue-deep));
  }
  .wordmark {
    position: absolute;
    display: flex;
    flex-direction: column;
    align-items: center;
    font-family: "Jost", sans-serif;
    text-transform: uppercase;
    line-height: 1;
  }
  .wordmark-dot { width: 52px; height: 52px; border-radius: 50%; margin-bottom: 22px; }
  .wordmark-name { font-size: 32px; font-weight: 500; letter-spacing: 0.3px; }
  .wordmark-tag { font-size: 17px; font-weight: 300; letter-spacing: 8px; margin-top: 5px; margin-right: -8px; }
  .card-front .wordmark { left: 30px; top: 77px; width: 198px; color: var(--brand-blue); }
  .card-front .wordmark-dot { background: var(--mark-grey); }
  .card-front .wordmark-tag { color: var(--tag-grey); }
  .card-back .wordmark { left: 0; top: 62px; width: 440px; color: var(--card-white); }
  .card-back .wordmark-dot { background: var(--card-white); width: 68px; height: 68px; margin-bottom: 24px; }
  .card-back .wordmark-name { font-size: 37px; }
  .card-back .wordmark-tag { font-size: 19px; letter-spacing: 10px; margin-right: -10px; margin-top: 4px; }

  .contact { position: absolute; left: 242px; top: 53px; color: var(--ink); font-size: 13px; line-height: 16px; }
  .contact-name { color: var(--brand-blue); font-weight: 600; font-size: 19px; line-height: 22px; }
  .contact-role { margin-bottom: 10px; }
  .contact-address { margin-bottom: 10px; }
  .contact-list { list-style: none; }
  .contact-list li { display: flex; align-items: center; gap: 6px; }
  .contact-list svg { width: 9px; height: 9px; fill: var(--brand-blue); flex: none; }
</style>
</head>
<body>
  <section class="card card-front" aria-label="Card front">
    <div class="wordmark">
      <span class="wordmark-dot"></span>
      <span class="wordmark-name">Lumenfield</span>
      <span class="wordmark-tag">Consulting</span>
    </div>
    <div class="contact">
      <p class="contact-name">Tom Verisco</p>
      <p class="contact-role">Managing Director</p>
      <p class="contact-address">48 Lantern Row<br>Melbourne VIC 3000</p>
      <ul class="contact-list">
        <li><svg viewBox="0 0 10 10"><rect x="2.5" y="0" width="5" height="10" rx="1"/><rect x="3.5" y="1.5" width="3" height="6" fill="#fff"/></svg>+61412 305 617</li>
        <li><svg viewBox="0 0 10 10"><path d="M0 3 Q5 0 10 3 L9 5 L7 4 L7 3 L3 3 L3 4 L1 5Z"/><rect x="2" y="5" width="6" height="4" rx="1"/></svg>+61 3 5550 4455</li>
        <li><svg viewBox="0 0 10 10"><rect x="1" y="3" width="8" height="6" rx="1"/><rect x="3" y="0" width="4" height="3"/></svg>+61 3 5550 4456</li>
        <li><svg viewBox="0 0 10 10"><rect x="0" y="2" width="10" height="6"/><path d="M0 2 L5 6 L10 2" fill="none" stroke="#fff" stroke-width="1"/></svg>info@lumenfield.example</li>
        <li><svg viewBox="0 0 10 10"><path d="M2 8 L8 2" stroke="#2a66bb" stroke-width="1.5"/><rect x="5.5" y="0.5" width="4" height="4" rx="1.5" fill="none" stroke="#2a66bb"/><rect x="0.5" y="5.5" width="4" height="4" rx="1.5" fill="none" stroke="#2a66bb"/></svg>www.lumenfield.example</li>
      </ul>
    </div>
  </section>

  <section class="card card-back" aria-label="Card back">
    <div class="wordmark">
      <span class="wordmark-dot"></span>
      <span class="wordmark-name">Lumenfield</span>
      <span class="wordmark-tag">Consulting</span>
    </div>
  </section>
</body>
</html>
```